vortane realty business card

We need a Business card for our new business. The logo was designed by ArtQuillo, and the text We want on the back is:
REAL ESTATE INVESTMENTS
- BUY, RENOVATE, SELL AND RENT RESIDENTIAL PROPERTIES
- FULL HOME REHABBING , REMODELING AND INTERIOR DESIGN
- HOME STAGING SERVICES
- WHOLESALE INVESTOR PROPERTIES
- MAKE CASH OFFERS ON HOUSES IN ANY CONDITION AND IN ANY SITUATION
- PRIVATE MONEY INVESTOR PROGRAMS WITH 6-12% RETURNS
- PAY CASH REWARDS FOR REFFERALS
- CONCIERGE SERVICE

```html
<!DOCTYPE html>
<html lang="en">
<head>
<meta charset="utf-8">
<title>Vortane Realty Business Card</title>
<link rel="stylesheet" href="https://fonts.googleapis.com/css2?family=Cabin:wght@400;600&family=Courier+Prime:wght@700&family=Arimo:wght@400;700&display=swap">
<style>
  :root {
    --card-front: #92c6cb;
    --ink-white: #ffffff;
    --tagline: #e3f1f2;
    --back-top: #ffffff;
    --back-bottom: #c8e8e7;
    --stage-band: #d6eeed;
    --heading: #8cc7cc;
    --list-light: #86c6cb;
    --list-dark: #3f97a2;
    --bullet: #8bc7cc;
  }
  * { margin: 0; padding: 0; box-sizing: border-box; }
  html, body { width: 1200px; height: 1000px; overflow: hidden; }
  body {
    position: relative;
    background: linear-gradient(180deg, #ffffff 0%, #fbfdfd 38%, var(--stage-band) 58%, var(--stage-band) 80%, #ffffff 100%);
    font-family: "Arimo", Arial, sans-serif;
  }

  /* Front side */
  .card-front {
    position: absolute; left: 222px; top: 86px; width: 731px; height: 406px;
    background: var(--card-front);
    color: var(--ink-white);
  }
  .brand {
    position: absolute; left: 0; right: 0; top: 214px; text-align: center;
  }
  .brand-name {
    font-family: "Cabin", sans-serif; font-weight: 400; font-size: 29px;
    letter-spacing: 0.5px; color: var(--ink-white); line-height: 1;
  }
  .brand-tagline {
    margin-top: 12px;
    font-family: "Cabin", sans-serif; font-size: 13.5px; letter-spacing: 1px;
    color: var(--tagline);
  }
  .contact-person {
    position: absolute; left: 44px; top: 313px; font-size: 18.5px; line-height: 23.5px;
  }
  .contact-person .person-name { font-weight: 700; }
  .contact-web {
    position: absolute; right: 42px; top: 336px; font-size: 18.5px; line-height: 23.5px;
    text-align: center;
  }

  /* Back side */
  .card-back {
    position: absolute; left: 235px; top: 544px; width: 727px; height: 408px;
    background: linear-gradient(180deg, var(--back-top) 0%, #f4fafa 20%, var(--back-bottom) 70%, var(--back-bottom) 100%);
  }
  .services-title {
    position: absolute; left: 0; right: 0; top: 62px; text-align: center;
    font-family: "Courier Prime", "Courier New", monospace; font-weight: 700;
    font-size: 25px; letter-spacing: 1.5px; word-spacing: 10px;
    color: var(--heading);
    text-shadow: 1px 1px 0 #5fa9b1, -1px -1px 0 #ffffff;
  }
  .services-list {
    position: absolute; left: 22px; top: 125px; list-style: none;
    font-family: "Cabin", sans-serif; font-weight: 600; font-size: 18.5px;
    line-height: 26.3px; letter-spacing: 0.3px;
  }
  .services-list li { position: relative; padding-left: 36px; }
  .services-list li::before {
    content: ""; position: absolute; left: 2px; top: 10px;
    width: 8px; height: 8px; border-radius: 50%; background: var(--bullet);
  }
  .services-list li:nth-child(1) { color: #86c6cb; }
  .services-list li:nth-child(2) { color: #7dbdc3; }
  .services-list li:nth-child(3) { color: #75b6bd; }
  .services-list li:nth-child(4) { color: #6aaeb6; }
  .services-list li:nth-child(5) { color: #5ea6af; }
  .services-list li:nth-child(6) { color: #4f9ea8; }
  .services-list li:nth-child(7) { color: #4799a3; }
  .services-list li:nth-child(8) { color: var(--list-dark); }
</style>
</head>
<body>
  <section class="card-front" aria-label="Business card front">
    <div class="brand">
      <div class="brand-name">VORTANE Realty</div>
      <div class="brand-tagline">REAL ESTATE SOLUTIONS</div>
    </div>
    <div class="contact-person">
      <div class="person-name">Name Name</div>
      <div>Address Address Address</div>
      <div>City</div>
    </div>
    <div class="contact-web">
      <div>+9999999999</div>
      <div>www.sitename.com</div>
    </div>
  </section>

  <section class="card-back" aria-label="Business card back">
    <h1 class="services-title">REAL ESTATE INVESTMENTS</h1>
    <ul class="services-list">
      <li>BUY, RENOVATE, SELL AND RENT RESIDENTIAL PROPERTIES</li>
      <li>FULL HOME REHABBING , REMODELING AND INTERIOR DESIGN</li>
      <li>HOME STAGING SERVICES</li>
      <li>WHOLESALE INVESTOR PROPERTIES</li>
      <li>MAKE CASH OFFERS ON HOUSES IN ANY CONDITION<br>AND IN ANY SITUATION</li>
      <li>PRIVATE MONEY INVESTOR PROGRAMS WITH 6-12% RETURNS</li>
      <li>PAY CASH REWARDS FOR REFFERALS</li>
      <li>CONCIERGE SERVICE</li>
    </ul>
  </section>
</body>
</html>
```